GUARANTEED WordPress design needed for a sassy, confident charisma coach!

We need a website design for Mira Haskett's brand new, responsive, Wordpress website.
Mira is a trainer / coach who teaches people how to be more charismatic and runs events, publishes video courses and has an ongoing video blog. Her old website is here: www.mirahaskett-example.co.uk ... but it's now time to have a much better site!
We have a strong idea about the technical components of the website, but we need a designer's eye to create a great style for the site (and provide layered PSD files which our developers will then convert to HTML and CSS).
Mira's brand is sassy, brave, warm and confident. The videos on her existing site give quite a good feel for her personality. We need a clean, stylish and compelling page that isn't too corporate and captures her personality. Every element needs to feel coherent, from fonts and headings to colours and spacing.
The following sites are not exactly what Mira wants (and certainly aren't right in terms of colours) but they give you an idea of the kind of people she is competing against and the area she is operating in:
http://www.fenna-troske.example/
http://brynwellow.example/
Ideally, you will have done something similar and be able to key in on exactly the kind of thing we want: we're not looking to reinvent the wheel. Hopefully you won't mind tweaking a few things if you are close to what we need.
More detail is provided in the word document attached. But in a nutshell we need: a banner, footer, sign-up strap, menu bar, signature and 4 different basic page types. We want bursts of bright colours, contrasted with black and white if possible - sorry we can't be more specific than that...
The word doc also contains some amateur mock-ups as well (the images are also just mockups at this stage) - but although these give a general sense of the structure what we are looking for, we are clearly not designers...so please help! We need a designer's touch!
Kind regards,
Tomas
PS The layered PSD versions of the mockup files are available on Quellbox: https://files.quellbox.example/sh/k27rpw4m1xqzv/QWxnEr8tLpVu3YcMd0aHs?dl=0
Project Deadline Extended Reason: We are looking for a polished, "designed" look. The mock-up that we have provided is just indicative of the features we want. Added Saturday, May 14, 2016
Entrepreneurs who need to sell themselves.
4 page

```html
<!DOCTYPE html>
<html lang="en">
<head>
<meta charset="utf-8">
<title>Mira Haskett – The Image &amp; Impact Specialist</title>
<link rel="stylesheet" href="https://fonts.googleapis.com/css2?family=Arimo:wght@400;700&family=Kaushan+Script&display=swap">
<style>
:root{
  --red:#e8262d;
  --red-dark:#c81d23;
  --yellow:#fbe67a;
  --sky:#55d2ef;
  --cyan:#3fc6ea;
  --coral:#f3705e;
  --green:#2fbe4c;
  --blue:#2aa6e0;
  --orange:#f06a2b;
  --ink:#1a1a1a;
  --grey:#6f6f6f;
  --grey-light:#e9e9e9;
  --grey-band:#b9b9b9;
  --white:#ffffff;
}
*{box-sizing:border-box;margin:0;padding:0}
html,body{width:1200px;height:2764px;overflow:hidden}
body{position:relative;background:var(--white);font-family:"Arimo",Arial,sans-serif;color:var(--ink)}
.abs{position:absolute}
.placeholder{position:absolute}

/* header */
.brand{left:40px;top:34px;display:flex;align-items:center;gap:14px}
.brand-mark{width:34px;height:34px;background:var(--red)}
.brand-name{font-size:40px;font-weight:700;color:var(--ink)}
.nav{left:390px;top:48px;width:770px;height:72px;background:var(--red);display:flex;justify-content:flex-end;align-items:center;gap:46px;padding-right:30px}
.nav a{color:var(--white);text-decoration:none;font-size:19px;font-weight:700;letter-spacing:.5px}

/* hero */
.hero{left:0;top:160px;width:1200px;height:360px;background:var(--white)}
.band{position:absolute;height:64px;display:flex;align-items:center;font-size:62px;font-weight:400;letter-spacing:2px;color:var(--ink)}
.band-attract{left:100px;top:80px;width:480px;background:var(--yellow);padding-left:44px}
.band-connect{left:140px;top:144px;width:480px;background:var(--sky);padding-left:90px}
.band-influence{left:100px;top:208px;width:500px;background:var(--coral);padding-left:70px}
.hero-arrow{position:absolute;top:160px;width:40px;height:64px;background:var(--red)}
.hero-arrow svg{display:block}

/* sign-up strip */
.optin{left:0;top:520px;width:1200px;height:340px;background:var(--cyan)}
.optin-copy{position:absolute;left:580px;top:74px;width:560px;font-size:25px;line-height:1.3;color:var(--ink)}
.optin-form{position:absolute;left:580px;top:190px;display:flex;gap:14px}
.field{width:250px;height:38px;background:var(--white);font-size:16px;padding:10px 14px;color:var(--ink)}
.optin-note{position:absolute;left:580px;top:240px;font-size:15px;color:var(--ink)}
.btn-submit{position:absolute;left:978px;top:236px;width:136px;height:34px;background:var(--red);color:var(--white);font-weight:700;font-size:17px;display:flex;align-items:center;justify-content:center}

/* tagline */
.tagline{left:0;top:868px;width:1200px;text-align:center;font-family:"Kaushan Script",cursive;font-size:46px;color:var(--ink)}

/* feature cards */
.card{position:absolute;top:950px;width:350px;height:320px;background:var(--white);border:1px solid var(--grey-light)}
.card-head{height:180px;position:relative;padding:12px 14px;color:var(--white);font-weight:700;font-size:27px;line-height:1.15}
.card-red .card-head{background:var(--red)}
.card-green .card-head{background:var(--green)}
.card-blue .card-head{background:var(--blue)}
.card-head .big{display:block;font-size:44px;color:var(--ink);margin-top:6px}
.card-title{font-size:16px;padding:10px 12px 4px;color:var(--ink)}
.card-text{font-size:12px;line-height:1.45;color:var(--grey);padding:0 12px}
.card-more{font-size:12px;color:var(--red);padding:8px 12px;font-weight:700}

/* about */
.section-bar{left:40px;top:1320px;width:780px;height:50px;background:var(--grey-band);color:var(--white);font-size:28px;font-weight:700;padding:10px 20px;letter-spacing:1px}
.about-heading{left:410px;top:1396px;width:410px;font-size:29px;font-weight:700;line-height:1.15;white-space:nowrap}
.about-text{left:410px;top:1446px;width:410px;font-size:18px;line-height:1.3;color:var(--ink)}
.about-text p{margin-bottom:22px}

/* sidebar */
.sidebar{left:860px;top:1320px;width:300px}
.side-title{font-size:32px;font-weight:700;color:var(--red)}
.side-tab{margin-top:6px;font-size:14px;font-weight:700;color:var(--red);border-bottom:2px solid var(--red);padding-bottom:4px}
.side-list{list-style:none;margin-top:12px}
.side-list li{font-size:14px;color:var(--red);font-weight:700;line-height:1.25;padding:8px 0;border-bottom:1px solid var(--grey-light)}
.side-list span{display:block;font-weight:400;color:var(--grey);font-size:12px}
.tags{display:flex;flex-wrap:wrap;gap:5px;margin-top:16px}
.tag{background:var(--red);color:var(--white);font-size:14px;padding:3px 6px}
.tag.l{font-size:22px;font-weight:700}
.tag.m{font-size:18px}
.promo{left:860px;top:1900px;width:300px;height:480px;background:linear-gradient(180deg,#f58a45,var(--orange))}
.promo-text{position:absolute;left:18px;top:20px;font-size:26px;font-weight:700;color:var(--white);line-height:1.1}
.promo-live{position:absolute;left:18px;top:250px;font-size:80px;font-weight:700;color:var(--white)}
.promo-note{position:absolute;left:150px;top:370px;font-size:20px;color:var(--white);line-height:1.1}
.promo-btn{position:absolute;left:18px;top:400px;width:110px;height:60px;background:var(--white);color:var(--orange);font-size:16px;font-weight:700;display:flex;align-items:center;justify-content:center;text-align:center;line-height:1.1}

/* videos */
.videos-title{left:40px;top:2090px;width:780px;text-align:center;font-size:30px;font-weight:700}
.video{position:absolute;top:2140px;width:380px;height:230px;background:linear-gradient(160deg,#cfc6bf,#8b7d78)}
.video-bar{position:absolute;left:0;bottom:0;width:100%;height:22px;background:rgba(0,0,0,.55)}
.dots{left:40px;top:2392px;width:780px;display:flex;justify-content:center;gap:10px}
.dot{width:16px;height:16px;border-radius:50%;border:2px solid var(--grey);background:var(--white)}
.dot.on{background:var(--grey)}

/* newsletter */
.newsletter{left:0;top:2440px;width:1200px;height:250px;background:var(--grey-light)}
.news-copy{position:absolute;left:0;top:30px;width:1200px;text-align:center;font-size:21px;font-weight:700;line-height:1.35}
.news-form{position:absolute;left:340px;top:120px;display:flex;gap:20px}
.news-form .field{width:220px;height:42px;border:1px solid #cfcfcf}
.btn-yes{position:absolute;left:820px;top:104px;width:80px;height:80px;border-radius:50%;background:var(--red);color:var(--white);font-weight:700;font-size:15px;display:flex;align-items:center;justify-content:center;text-align:center;line-height:1.1}
.news-sad{position:absolute;left:0;top:186px;width:1200px;text-align:center;font-size:14px;color:var(--grey)}
.social{position:absolute;left:512px;top:212px;display:flex;gap:8px}
.social i{width:22px;height:22px;background:var(--blue);display:block}
.social i:nth-child(2){background:var(--red)}
.social i:nth-child(3){background:var(--grey)}
.social i:nth-child(5){background:var(--orange)}
.footer-links{left:0;top:2716px;width:1200px;display:flex;justify-content:center;gap:60px;font-size:12px;color:var(--grey)}
</style>
</head>
<body>

<header>
  <div class="abs brand"><span class="brand-mark"></span><span class="brand-name">Mira Haskett</span></div>
  <nav class="abs nav">
    <a href="#">EVENTS</a><a href="#">WORK WITH ME</a><a href="#">CORPORATE</a><a href="#">ABOUT</a><a href="#">CONTACT</a>
  </nav>
</header>

<section class="abs hero">
  <div class="band band-attract">ATTRACT</div>
  <div class="band band-connect">CONNECT</div>
  <div class="band band-influence">INFLUENCE</div>
  <div class="placeholder" role="img" aria-label="Portrait of the coach in a red dress, arms crossed" style="left:740px;top:0;width:330px;height:360px;background:linear-gradient(180deg,#e9d6cf,#d9443d)"></div>
  <div class="hero-arrow" style="left:0"><svg width="40" height="64"><polygon points="28,18 12,32 28,46" fill="#fff"/></svg></div>
  <div class="hero-arrow" style="left:1160px"><svg width="40" height="64"><polygon points="12,18 28,32 12,46" fill="#fff"/></svg></div>
</section>

<section class="abs optin">
  <div class="placeholder" role="img" aria-label="Laptop showing the free training video" style="left:130px;top:30px;width:350px;height:270px;background:linear-gradient(170deg,#5a5a5a,#1e1e1e)"></div>
  <p class="optin-copy">Learn how to unlock the superpower* of your charisma and win all the business you want with this free training.</p>
  <div class="optin-form"><div class="field">NAME</div><div class="field">EMAIL ADDRESS</div></div>
  <p class="optin-note">* Promise to only use your powers for good</p>
  <div class="btn-submit">SUBMIT</div>
</section>

<h2 class="abs tagline">The Image &amp; Impact Specialist!</h2>

<article class="card card-red" style="left:40px">
  <div class="card-head">PUBLIC SPEAKING...<span class="big" style="font-size:38px;color:var(--ink);margin-top:24px">MADE<br>EASY :)</span>
    <div class="placeholder" role="img" aria-label="Speaker on stage with microphone" style="left:190px;top:40px;width:150px;height:140px;background:linear-gradient(180deg,#f07a7e,#b8181f)"></div>
  </div>
  <p class="card-title">Public speaking...made easy</p>
  <p class="card-text">Simple steps to calm nerves, own the room and speak with ease, warmth and real presence every time you stand up.</p>
  <p class="card-more">READ MORE &rarr;</p>
</article>

<article class="card card-green" style="left:425px">
  <div class="card-head">HOW TO START EVERY DAY IN THE RIGHT FRAME OF MIND!<span class="big">5 HOT TIPS</span></div>
  <p class="card-title">How to start every day in the right frame of mind</p>
  <p class="card-text">Five quick habits to set your mood, lift your energy and walk into each day feeling bold, calm and ready.</p>
  <p class="card-more">READ MORE &rarr;</p>
</article>

<article class="card card-blue" style="left:810px">
  <div class="card-head">TAKE CHARGE OF YOUR STYLE...<br><span style="font-size:22px">...BOOST YOUR</span><br><span style="font-size:30px">CONFIDENCE</span>
    <div class="placeholder" role="img" aria-label="Rail of colourful clothes" style="left:230px;top:60px;width:110px;height:110px;background:linear-gradient(180deg,#f3c2d9,#7c5bd6)"></div>
  </div>
  <p class="card-title">Take charge of your style...boost your confidence</p>
  <p class="card-text">Find the colours, cuts and looks that suit you so you feel great, look sharp and make a strong first impression.</p>
  <p class="card-more">READ MORE &rarr;</p>
</article>

<div class="abs section-bar">ABOUT ME......</div>
<div class="placeholder" role="img" aria-label="Full-length portrait of the coach in a black and white dress" style="left:40px;top:1390px;width:340px;height:640px;background:linear-gradient(180deg,#efefef,#cfcfcf)"></div>
<h3 class="abs about-heading">Lorem ipsum dolor sit amet</h3>
<div class="abs about-text">
  <p>Lorem ipsum dolor sit amet, consectetuer adipiscing elit, sed diam nonummy nibh euismod tincidunt ut laoreet dolore magna aliquam erat volutpat. Ut wisi enim ad minim veniam, quis nostrud exerci tation ullamcorper suscipit lobortis nisl ut aliquip ex ea commodo consequat. Duis autem vel eum iriure dolor in hendrerit in vulputate velit esse molestie consequat, vel illum dolore eu feugiat nulla facilisis at vero eros et accumsan et iusto odio dignissim qui blandit praesent luptatum zzril delenit augue duis dolore te feugait nulla facilisi. Nam liber tempor cum soluta nobis eleifend option congue nihil imperdiet doming id quod mazim placerat facer possim assum.</p>
  <p>Lorem ipsum dolor sit amet, consectetuer adipiscing elit, sed diam nonummy nibh euismod tincidunt ut laoreet dolore magna aliquam erat volutpat. Ut wisi enim ad minim veniam, quis nostrud exerci tation ullamcorper suscipit lobortis nisl ut aliquip ex ea commodo consequat.</p>
</div>

<aside class="abs sidebar">
  <div class="side-title">MIRA SAYS...</div>
  <div class="side-tab">POPULAR</div>
  <ul class="side-list">
    <li>Be more dog: 3 lessons we could learn from our best friends<span>14 June 2016</span></li>
    <li>Are you hiding your voice behind bad habits?<span>2 June 2016</span></li>
    <li>Nail the room: how to stand out at any event<span>24 May 2016</span></li>
    <li>Stop waiting and start being seen, right now<span>12 May 2016</span></li>
    <li>Bright colours, bold style - no more grey days<span>3 May 2016</span></li>
  </ul>
  <div class="tags">
    <span class="tag">body language</span><span class="tag l">capsule wardrobe</span><span class="tag">confidence</span><span class="tag">charisma</span><span class="tag m">power pose</span><span class="tag">first impressions</span><span class="tag">voice</span><span class="tag l">rapport</span><span class="tag">speaking</span><span class="tag">style</span><span class="tag">colour</span>
  </div>
</aside>

<div class="placeholder promo" role="img" aria-label="Promotion for the live charisma event with the coach on stage">
  <div class="promo-text">UNLOCK<br>THE<br>SUPERPOWER<br>OF<br>CHARISMA</div>
  <div class="promo-live">LIVE</div>
  <div class="promo-note">* Only 6<br>places left</div>
  <div class="promo-btn">LEARN<br>MORE</div>
</div>

<h2 class="abs videos-title">WATCH VIDEOS</h2>
<div class="video" role="img" aria-label="Video still of the coach talking to camera" style="left:40px"><div class="video-bar"></div></div>
<div class="video" role="img" aria-label="Video still of the coach presenting a tip" style="left:440px"><div class="video-bar"></div></div>
<div class="abs dots"><span class="dot on"></span><span class="dot"></span><span class="dot"></span><span class="dot"></span></div>

<section class="abs newsletter">
  <p class="news-copy">Hey! Don't go without signing up because you'll miss out on exclusive<br>offers, awesome tips, and weekly motivation in my fab newsletter *.</p>
  <div class="news-form"><div class="field">First name</div><div class="field">Email address</div></div>
  <div class="btn-yes">YES<br>PLEASE!</div>
  <p class="news-sad">* And that'll make me sad :(</p>
  <div class="social"><i></i><i></i><i></i><i></i><i></i><i></i></div>
</section>

<footer class="abs footer-links">
  <span>© 2016 mirahaskett-example.co.uk</span><span>PRIVACY POLICY</span><span>TERMS &amp; CONDITIONS</span><span>DISCLAIMER</span>
</footer>

</body>
</html>
```